Seasoning Mix Food Packet Design

Ok, let's get to work! This is a new food company based in New York City. Our first product that we are introducing is a dry seasoning rub for fried chicken wings. Let me give you some history about the seasoning. This seasoning was a secret recipe from my grandfather that was passed down to his kids and grandkids. He worked as a cook in a famous restaurant and bar named "LanternLeaf". Located in Port of Spain Trinidad, LanternLeaf sold chicken, french fries and alcohol. Little to behold, the "fried chicken" became the staple for the restaurant. The news about the flavorful taste of the chicken spread through the communities and towns. Lines stretched down the block waiting to buy my grandfather's seasoned fried chicken. It was considered the best Chinese fried chicken by many.
I am packaging the seasoning blend in a 8X12cm heat seal open top shiny aluminum bag/packet with a transparent back. I need you to design the front of the packet based on the inner size dimension below.
Package Dimensions:
Outer Size:8x12cm/3.1x4.7''
Inner Size: 7x10.3cm/2.7x4''
Product Name : Mr. Talbot's LanternLeaf Fried Chicken (Seasoning Mix)
Overall goal is to get the vendor to print your design onto the aluminum packets.
Attachments:
1. Photos of 8X12cm aluminum packets
2. Rough draft of product package design
Target Market(s)
Asian Market
Industry/Entity Type
Food Store
Logo Text
Mr. Talbot's LanternLeaf Fried Chicken (Seasoning Mix)
Logo styles of interest
Pictorial/Combination Logo
Abstract Logo
Wordmark Logo
Look and feel
Each slider illustrates characteristics of the customer's brand and the style your logo design should communicate.

```html
<!DOCTYPE html>
<html lang="en">
<head>
<meta charset="utf-8">
<title>Mr. Talbot's LanternLeaf Fried Chicken – Seasoning Mix</title>
<link rel="stylesheet" href="https://fonts.googleapis.com/css2?family=Caesar+Dressing&family=Pinyon+Script&family=Allura&family=Arimo:wght@700&display=swap">
<style>
  :root {
    --paper: #ffffff;
    --ink: #111111;
    --chili: #c8191e;
    --frame: #8e1417;
    --gold: #e6b64c;
    --gold-deep: #c9a25e;
    --gold-pale: #fff7e0;
    --photo-warm: #b5502a;
    --photo-light: #e8b07a;
  }
  * { margin: 0; padding: 0; box-sizing: border-box; }
  html, body { width: 800px; height: 1200px; overflow: hidden; background: var(--paper); }
  .packet { position: relative; width: 800px; height: 1200px; background: var(--paper); }

  .brand-name {
    position: absolute; top: 140px; left: 0; width: 800px;
    text-align: center;
    font-family: "Pinyon Script", cursive;
    font-size: 70px; line-height: 1;
    color: var(--ink);
  }

  .title-band {
    position: absolute; top: 272px; left: 0; width: 800px; height: 86px;
    background: linear-gradient(90deg, var(--paper) 0%, var(--gold) 18%, var(--gold-pale) 55%, var(--gold) 80%, var(--paper) 100%);
    display: flex; align-items: center; justify-content: center;
  }
  .product-title {
    font-family: "Caesar Dressing", fantasy;
    font-size: 70px; letter-spacing: 2px;
    color: var(--chili);
  }

  .product-type {
    position: absolute; top: 448px; left: 0; width: 800px;
    text-align: center;
    font-family: "Arimo", Arial, sans-serif; font-weight: 700;
    font-size: 40px; color: var(--chili);
  }

  .hero-photo {
    position: absolute; top: 507px; left: 173px; width: 454px; height: 293px;
    border: 7px solid var(--frame);
    background: radial-gradient(ellipse at 45% 55%, var(--photo-warm) 0%, #a23c1e 45%, var(--photo-light) 100%);
  }

  .tagline {
    position: absolute; top: 712px; left: 310px; width: 320px;
    font-family: "Allura", cursive;
    font-size: 92px; line-height: 0.95;
    color: var(--chili);
    -webkit-text-stroke: 0;
    text-shadow: 0 0 4px #fff, 0 0 4px #fff, 0 0 4px #fff;
  }
  .tagline span { display: block; }
  .tagline .line-two { padding-left: 70px; }

  .net-weight {
    position: absolute; top: 1098px; left: 48px; width: 704px; height: 50px;
    background: linear-gradient(90deg, var(--gold-deep), #d9b878 50%, var(--gold-deep));
    display: flex; align-items: center; justify-content: flex-end;
    padding-right: 22px;
    font-family: "Arimo", Arial, sans-serif; font-weight: 700;
    font-size: 27px; color: var(--paper);
  }
</style>
</head>
<body>
  <main class="packet">
    <h1 class="brand-name">Mr. Talbot's LanternLeaf</h1>
    <div class="title-band"><h2 class="product-title">FRIED CHICKEN</h2></div>
    <p class="product-type">Seasoning Mix</p>
    <div class="hero-photo" role="img" aria-label="Photo of glazed fried chicken wings on a plate with fresh salad"></div>
    <p class="tagline"><span>Flavorful</span><span class="line-two">Taste</span></p>
    <div class="net-weight">NET WT. 1.09 OZ (31g)</div>
  </main>
</body>
</html>
```